Byteloft - Your IT support team - online sales website design concept

Byteloft aims to provide home and small business users with high quality, friendly and affordable IT support.

We are delivering this service through the website. Users will choose a support service that they want, enter some details, make a payment and then be connected to our support team member who will resolve their problem and discuss their IT with them by remotely controlling their computer and speaking to them on the phone.

This design project is to develop the website design concept which will:

# Give the user confidence that byteloft are a legitimate business giving premium yet good value IT support.
# Inform the users of our IT services.
# Encourage the user to try our services.
# Look fun, interesting, modern, respectable and trustworthy.

We intend to offer 4 core 'products' to our users, these are:
# Virus removal – We will clean your PC then protect it for the future
# Computer Speed Up – Optimise you PC to get the most out of it
# Skyvault your IT- auto backup of PC with remote access to documents, pictures, videos and email
# IT Support – to fix a problem or we can just help out

We are open to any fun or interesting ways of getting this message across to users.

We have the following idea which could be useful but does not have to be used in design concepts:

Perhaps a home/detached house on the front page with a cloud in the sky for our cloud service, a fast car on the drive or something to demonstrate computer speed up, a gremlin in the drain for virus removal and our byteloft yellow waves from our logo emanating towards the house as our general IT support offering. Maybe having some movement or information on mouse over.

We like the idea of real life images embedded into the page similar to this:

http://www.prolivasad.cz/

But, ideas could be cartoon based or whatever you think will look good. Any interesting concepts are welcome.

We want to have our 4 'products' clearly displayed on the home page. They could be in 4 boxes beneath some nice image or incorporated into a single nice image/cartoon or graphic. If incorporated into one graphic/cartoon/image we would have clickable areas of the image.

We want it to be clear to visitors what it is we are offering - IT support to remotely solve a computer/Tablet/smartphone issue and that we are "Online now to fix your problem".

We might also want to feature 4 features/benefits:

UK Based Engineers (with GB flag)
Remote IT Support
Premium Support
Money Back Guarantee

We have a logo already which is attached. We would like a homepage design encompassing the features set out above, a second page design to be used as the main page when you click on one of the 4 'products' and also a general content page design so that we have a theme for the site. We just want these designs as images for this project.

Thank you for your interest.

Reason: 10 days was never long enough and we needed more time to respond to designers.

Reason: I've been away on holiday and I want some more time to respond to designers. Thanks, Colin

Target Market(s)

Home and small business users.

Industry/Entity Type

Small Business

Requirements
Must have
• We would like an area, to show whether we are open and online or not. When staff are available to deliver remote support the site should clearly show that staff are online working and available now to support. When we are offline the site should also show this.

We will offer our users a "Money Back Guarantee"; if they are not happy with the work that we do for them we will refund them.

```html
<!DOCTYPE html>
<html lang="en">
<head>
<meta charset="utf-8">
<title>Byteloft – Your IT support team</title>
<link rel="stylesheet" href="https://fonts.googleapis.com/css2?family=Open+Sans:wght@300;400;600;700&family=Shadows+Into+Light+Two&display=swap">
<style>
:root{
  --yellow:#f5c518;
  --gold:#d4a514;
  --ink:#1e1e1e;
  --text:#3a3a3a;
  --hero:#1f1f1f;
  --white:#ffffff;
  --grey-top:#ebebeb;
  --grey-bottom:#fbfbfb;
  --rule:#e0e0e0;
  --footer:#9e9e9e;
}
*{margin:0;padding:0;box-sizing:border-box}
html,body{width:1200px;height:1187px;overflow:hidden;background:var(--white)}
body{position:relative;font-family:"Open Sans",Arial,sans-serif;color:var(--ink)}
a{color:inherit;text-decoration:none}
.abs{position:absolute}

/* header */
.site-header{position:absolute;left:0;top:0;width:1200px;height:119px;background:var(--white);border-bottom:2px solid #333}
.brand{position:absolute;left:116px;top:30px;display:flex;align-items:center;gap:10px}
.brand-mark{width:14px;height:14px;border-radius:50%;background:var(--yellow)}
.brand-name{font-size:46px;font-weight:700;color:var(--yellow);letter-spacing:-1px;line-height:1}
.brand-tagline{position:absolute;left:182px;top:84px;font-size:14px;color:var(--text);letter-spacing:1px}
.main-nav{position:absolute;top:55px;left:673px;display:flex;align-items:center;font-size:13px}
.main-nav a{display:block;height:30px;line-height:30px;color:var(--ink)}
.main-nav .is-active{width:79px;text-align:center;border-radius:8px;background:var(--yellow);color:var(--white)}
.main-nav .about{margin-left:50px}
.main-nav .signup{margin-left:54px}
.guarantee-badge{position:absolute;left:1016px;top:34px}

/* hero */
.hero{position:absolute;left:0;top:119px;width:1200px;height:510px;background:var(--hero)}
.hero svg{position:absolute;left:0;top:0}
.hero-title{position:absolute;left:390px;top:210px;width:400px;text-align:center;color:var(--white);font-size:38px;font-weight:600;line-height:40px}
.product-label{position:absolute;font-family:"Shadows Into Light Two",cursive;color:var(--yellow);font-size:27px;white-space:nowrap;transform:translateX(-50%)}

/* intro */
.intro{position:absolute;left:0;top:629px;width:1200px;height:256px;text-align:center}
.intro h1{position:absolute;left:150px;top:30px;width:880px;font-size:30px;font-weight:300;line-height:37px}
.intro h1 strong{font-weight:700}
.intro p{position:absolute;left:150px;top:128px;width:900px;font-size:16.5px;font-weight:300;line-height:19px}
.btn-read{position:absolute;left:505px;top:193px;width:144px;height:33px;line-height:33px;font-size:17px;color:#3a2a00;background:linear-gradient(#ffd400,#f7b500);border:1px solid #e8a800}

/* info */
.info{position:absolute;left:0;top:885px;width:1200px;height:247px;background:linear-gradient(var(--grey-top),var(--grey-bottom))}
.info h2{position:absolute;font-size:24px;font-weight:400;color:var(--ink)}
.welcome-text{position:absolute;left:134px;top:63px;width:560px;font-size:12.5px;line-height:20px;color:var(--text)}
.text-link{position:absolute;font-size:12px;color:var(--text);text-decoration:underline}
.news-item{position:absolute;left:803px;width:285px;height:72px;border-bottom:1px solid var(--rule)}
.news-num{position:absolute;left:0;top:2px;font-size:24px;font-weight:300;color:var(--yellow)}
.news-text{position:absolute;left:35px;top:0;width:250px;font-size:12.5px;line-height:20px;color:var(--text)}

/* footer */
.site-footer{position:absolute;left:0;top:1132px;width:1200px;height:55px;background:var(--footer);color:var(--white);font-size:11px}
.footer-nav{position:absolute;left:139px;top:20px}
.footer-nav span{margin:0 4px}
.copyright{position:absolute;right:116px;top:20px}
</style>
</head>
<body>

<header class="site-header">
  <a class="brand" href="#"><span class="brand-name">byteloft</span><span class="brand-mark"></span></a>
  <div class="brand-tagline">your IT support team</div>
  <nav class="main-nav">
    <a class="is-active" href="#">HOME</a>
    <a class="about" href="#">ABOUT US</a>
    <a class="signup" href="#">SIGN UP</a>
  </nav>
  <svg class="guarantee-badge" width="68" height="68" viewBox="0 0 68 68" role="img" aria-label="Money back guarantee seal">
    <circle cx="34" cy="34" r="33" fill="#e8a900"/>
    <circle cx="34" cy="34" r="24" fill="#f7c733" stroke="#333" stroke-width="2"/>
  </svg>
</header>

<section class="hero">
  <svg width="1200" height="510" viewBox="0 0 1200 510">
    <ellipse cx="590" cy="262" rx="235" ry="166" fill="none" stroke="var(--gold)" stroke-width="3"/>
    <!-- IT support: phone with 24 -->
    <g transform="translate(588,99)">
      <circle r="50" fill="var(--hero)"/>
      <path d="M-24,-33 A40,40 0 1 1 14,38" fill="none" stroke="#fff" stroke-width="7"/>
      <text x="10" y="9" text-anchor="middle" font-family="Open Sans,sans-serif" font-weight="700" font-size="28" fill="#fff">24</text>
      <path d="M-40,-16 q-6,22 14,44 q20,18 40,18 l8,-10 l-14,-12 l-9,6 q-14,-6 -26,-24 l6,-10 l-12,-16 z" fill="#fff"/>
    </g>
    <!-- Virus removal: tick box -->
    <g transform="translate(340,240)">
      <circle r="52" fill="var(--hero)"/>
      <rect x="-38" y="-28" width="60" height="60" rx="6" fill="none" stroke="#fff" stroke-width="8"/>
      <path d="M-26,0 l16,18 l40,-58" fill="none" stroke="var(--hero)" stroke-width="18"/>
      <path d="M-26,0 l16,18 l40,-58" fill="none" stroke="#fff" stroke-width="9"/>
    </g>
    <!-- Cloud backup -->
    <g transform="translate(823,238)">
      <rect x="-58" y="-45" width="116" height="82" fill="var(--hero)"/>
      <path d="M-46,33 a20,20 0 0 1 0,-40 a26,26 0 0 1 32,-18 a30,30 0 0 1 56,18 a20,20 0 0 1 2,40 z" fill="#fff"/>
      <path d="M0,-8 l-14,26 h9 v22 h10 v-22 h9 z" fill="var(--hero)" transform="rotate(180 0 15)"/>
    </g>
    <!-- Computer speed: paper plane -->
    <g transform="translate(575,405)">
      <rect x="-52" y="-35" width="104" height="72" fill="var(--hero)"/>
      <path d="M-48,3 L50,-32 L26,35 L0,16 L-12,32 L-14,10 Z" fill="none" stroke="#fff" stroke-width="6" stroke-linejoin="round"/>
      <path d="M-14,10 L50,-32 M0,16 L-12,32" stroke="#fff" stroke-width="5"/>
    </g>
  </svg>
  <div class="hero-title">Your Remote IT<br>Support Team</div>
  <div class="product-label" style="left:595px;top:14px">IT Support</div>
  <div class="product-label" style="left:298px;top:288px">Virus Removal</div>
  <div class="product-label" style="left:905px;top:278px">Cloud Backup</div>
  <div class="product-label" style="left:586px;top:448px">Computer Speed</div>
</section>

<section class="intro">
  <h1>We offering - IT support to remotely solve a <strong>Computer</strong>, <strong>Tablet</strong> &amp; <strong>Smartphone</strong> issue</h1>
  <p>Using only modern technologies and our experience, we can help clients get the all importantcommunication part of their business to the next level. All this while never having to move one finger, because we take care of all the following:</p>
  <a class="btn-read" href="#">Read More</a>
</section>

<section class="info">
  <h2 style="left:133px;top:28px">Welcome to Byteloft</h2>
  <p class="welcome-text">Contrairement à une opinion répandue, le Lorem Ipsum n'est pas simplement du texte aléatoire. Il trouve ses racines dans une oeuvre de la littérature latine classique datant de 45 av. J.-C., le rendant vieux de 2000 ans. Un professeur du Ashgrove College, en Virginie, s'est intéressé à un des mots latins les plus obscurs, consectetur, extrait d'un passage.</p>
  <a class="text-link" href="#" style="left:135px;top:157px">Read More</a>

  <h2 style="left:838px;top:28px">News</h2>
  <div class="news-item" style="top:64px">
    <span class="news-num">01</span>
    <p class="news-text">Contrairement à une opinion répandue, le Lorem Ipsum n'est pas simplement du texte</p>
  </div>
  <div class="news-item" style="top:136px">
    <span class="news-num">02</span>
    <p class="news-text">Contrairement à une opinion répandue, le Lorem Ipsum n'est pas simplement du texte</p>
  </div>
  <a class="text-link" href="#" style="left:1022px;top:217px">View more</a>
</section>

<footer class="site-footer">
  <nav class="footer-nav">
    <a href="#">Home</a><span>|</span><a href="#">About Us</a><span>|</span><a href="#">Services</a><span>|</span><a href="#">Products</a><span>|</span><a href="#">Contact &nbsp;Us</a>
  </nav>
  <div class="copyright">© 2013 byteloft. All Rights Reserved. Privacy Policy</div>
</footer>

</body>
</html>
```